Friseur sucht Heftcover für Tipps zur natürlichen Haarpflege
Zielgruppe
Wir sind ein Friseur auf natürlicher Basis und arbeiten ausschließlich mit Naturprodukten.
Hier in diesem Heft sind alle unsere Haartipps zur natürlichen Haarpflege zusammengefasst. Das Heftchen bekommt jeder Kunde aus dem Studio zur Pflege für zuhause.
Zielgruppe sind Frauen im Alter zwischen 30 und 55.
Aufgabenstellung
Unser grundsätzliches Design ist eher schlank und neutral. Das Haarkonzept-Heft soll als Produkt in unser Sortiment einfließen und sieht als Foto eher unattraktiv aus. Außerdem soll es eventuell auch als E-Book erscheinen.
Eigentlich soll es ein typisches aber ansehnliches Produktbild eines typischen E-Books/Buchcovers werden.
Wir brauchen hier eine einfache aber attraktive Darstellung dieser weißen Broschüre. Hintergrund soll ebenfalls oder falls möglich weiß bleiben.

```html
<!DOCTYPE html>
<html lang="de">
<head>
<meta charset="utf-8">
<title>Silva Pura – Haarpflege Heftcover Nr. 1 und Nr. 2</title>
<link rel="stylesheet" href="https://fonts.googleapis.com/css2?family=Marcellus&family=Montserrat:wght@800&display=swap">
<style>
  :root {
    --page: #ffffff;
    --ink: #111111;
    --paper: #ffffff;
    --sand-light: #f4d6bb;
    --sand-deep: #c8906b;
    --bronze-dark: #9a5f3d;
    --bronze-light: #d9a47c;
    --sky-light: #cfe3e8;
    --sky-deep: #a9cbd3;
    --teal-dark: #6fa4aa;
    --teal-light: #a8ccd1;
    --headline: #ffffff;
  }
  * { box-sizing: border-box; margin: 0; padding: 0; }
  html, body { width: 960px; height: 1200px; overflow: hidden; background: var(--page); }
  .canvas {
    position: relative;
    width: 960px; height: 1200px;
    display: flex; justify-content: center; align-items: center; gap: 60px;
  }
  .cover {
    position: relative;
    width: 400px; height: 566px;
    background: var(--paper);
    box-shadow: 0 14px 34px rgba(0,0,0,0.12);
    overflow: hidden;
  }
  .cover__brand {
    position: absolute; top: 0; left: 0; width: 297px; height: 90px;
    display: flex; align-items: center; justify-content: flex-end;
    padding-right: 4px;
    font-family: "Marcellus", serif;
    font-size: 33px; letter-spacing: 0.5px;
    color: var(--ink);
  }
  .cover__photo {
    position: absolute; top: 90px; left: 0; width: 297px; height: 476px;
  }
  .cover--one .cover__photo { background: radial-gradient(ellipse at 60% 55%, var(--sand-deep) 0%, #e2b08c 45%, var(--sand-light) 100%); }
  .cover--two .cover__photo { background: radial-gradient(ellipse at 55% 50%, #e3bfa0 0%, #d8c9bd 35%, var(--sky-light) 70%, var(--sky-deep) 100%); }
  .cover__headline {
    position: absolute; top: 102px; left: 0; width: 281px;
    text-align: right;
    font-family: "Marcellus", serif;
    font-size: 25px; line-height: 28px;
    color: var(--headline);
  }
  .cover__strip {
    position: absolute; top: 0; right: 0; width: 103px; height: 514px;
    background: var(--paper);
  }
  .cover__foot {
    position: absolute; bottom: 0; right: 0; width: 103px; height: 52px;
  }
  .cover--one .cover__foot { background: var(--sand-light); }
  .cover--two .cover__foot { background: var(--sky-light); }
  .cover__issue {
    position: absolute; left: 351px; top: 392px;
    transform: translate(-50%, -50%) rotate(-90deg);
    font-family: "Montserrat", sans-serif; font-weight: 800;
    font-size: 62px; letter-spacing: 2px; white-space: nowrap;
    -webkit-background-clip: text; background-clip: text; color: transparent;
  }
  .cover--one .cover__issue { background-image: linear-gradient(90deg, var(--bronze-dark), var(--bronze-light) 50%, var(--bronze-dark)); }
  .cover--two .cover__issue { background-image: linear-gradient(90deg, var(--bronze-dark) 0%, var(--bronze-light) 35%, var(--teal-light) 55%, var(--teal-dark)); }
</style>
</head>
<body>
<main class="canvas">
  <article class="cover cover--one">
    <div class="cover__photo" role="img" aria-label="Foto: zwei lächelnde Frauen Wange an Wange vor warmem Sandton"></div>
    <div class="cover__brand">Silva Pura</div>
    <h2 class="cover__headline">Haut &amp; Haar<br>in Harmonie</h2>
    <div class="cover__strip"></div>
    <div class="cover__foot"></div>
    <div class="cover__issue">Nr. 1</div>
  </article>
  <article class="cover cover--two">
    <div class="cover__photo" role="img" aria-label="Foto: lächelnde Frau mit hochgestecktem Haar vor hellblauem Hintergrund"></div>
    <div class="cover__brand">Silva Pura</div>
    <h2 class="cover__headline">Haut &amp; Haar<br>in Harmonie</h2>
    <div class="cover__strip"></div>
    <div class="cover__foot"></div>
    <div class="cover__issue">Nr. 2</div>
  </article>
</main>
</body>
</html>
```